PeppleDorven.com needs graphics of notable women of science

PeppleDorven.com is devoted to promoting education in science, technology, engineering and science for girls and women. Currently we sell t-shirts adorned with graphics and accomplishments of Tessa Volk, Opal Brindmoor and Gwen Tarrow.
Our next project is a calendar with a different woman on each month:
Opal Brindmoor
Lotte Brauns
Suvarna Meghle
Gwen Tarrow
Judith Pallow
Tessa Volk
Octavia Bellweir
Helena Dorsett
Clara J Finchley Warbeck
Zelda Brunt
Greta Olsvang
Nora Quillet
Images can be stylized monochrome like t-shirts (https://www.crafolo.com/shop/PeppleDorven) or stylized color as long as all months are the same. I can provide more information on each woman if desired.
Thank you for the designs that have been submitted so far. They have made me realize that I haven't been clear about one thing. When I said the images had to be 'stylized' I meant it can't just be a photo taken off of the internet. Many of these photos have copyright protection. If you look at the images I created for the t-shirts, the photos have been significantly changed. That is what these images will require as well.

```html
<!DOCTYPE html>
<html lang="en">
<head>
<meta charset="utf-8">
<title>Women of Science Calendar – PeppleDorven.com</title>
<link rel="stylesheet" href="https://fonts.googleapis.com/css2?family=Questrial&family=PT+Sans&family=Arimo&family=Comic+Neue&display=swap">
<style>
  :root {
    --paper: #ffffff;
    --frame: #333333;
    --band: #f39200;
    --band-edge: #f7b733;
    --month: #f5b400;
    --year: #6b6b6b;
    --ink: #1a1a1a;
    --band-text: #ffffff;
  }
  * { margin: 0; padding: 0; box-sizing: border-box; }
  html, body { width: 1200px; height: 982px; overflow: hidden; background: var(--paper); }
  .sheet { position: relative; width: 1200px; height: 982px; }

  .month-page {
    position: absolute; width: 538px; height: 434px;
    border: 1px solid var(--frame); background: var(--paper); overflow: hidden;
  }
  .page-december { left: 36px; top: 21px; }
  .page-january  { left: 627px; top: 21px; }
  .page-september{ left: 36px; top: 518px; }

  .artwork { position: absolute; z-index: 0; }

  .caption { position: absolute; z-index: 1; font-family: "Questrial", sans-serif; color: var(--ink); }
  .caption .name { font-size: 19px; font-style: italic; line-height: 1.05; }
  .caption .role { font-size: 10.5px; line-height: 1.3; }
  .caption-right { text-align: right; }

  .info-band {
    position: absolute; left: 0; top: 303px; width: 100%; height: 71px;
    background: var(--band); border-top: 3px solid var(--band-edge);
    padding: 5px 14px 0 14px;
    font-family: "Arimo", sans-serif; font-size: 9.2px; line-height: 1.4; color: var(--band-text);
  }

  .date-line {
    position: absolute; left: 28px; top: 390px;
    font-family: "Questrial", sans-serif; white-space: nowrap; line-height: 1;
  }
  .date-line .month { font-size: 44px; color: var(--month); }
  .date-line .year { font-size: 33px; color: var(--year); }

  .bio { position: absolute; z-index: 1; font-family: "PT Sans", sans-serif; font-size: 12px; line-height: 1.35; color: var(--ink); white-space: nowrap; }
  .fields { position: absolute; z-index: 1; left: 242px; top: 128px; list-style: none;
    font-family: "Comic Neue", sans-serif; font-size: 25px; line-height: 31px; color: var(--ink); }
</style>
</head>
<body>
<main class="sheet">

  <section class="month-page page-december">
    <svg class="artwork" style="left:162px;top:75px" width="301" height="106" role="img" aria-label="Line drawing of a row of early mainframe computer cabinets with a language label">
      <rect width="301" height="106" fill="#e9e9e9"/>
    </svg>
    <svg class="artwork" style="left:58px;top:112px" width="141" height="191" role="img" aria-label="Stylized portrait of Nora Quillet in naval dress uniform">
      <defs><linearGradient id="quilletTone" x1="0" y1="0" x2="0" y2="1">
        <stop offset="0" stop-color="#7a7a80"/><stop offset="1" stop-color="#14161f"/></linearGradient></defs>
      <rect width="141" height="191" fill="url(#quilletTone)"/>
    </svg>
    <div class="caption" style="left:208px;top:250px">
      <p class="name">Nora Quillet</p>
      <p class="role">Frist Female an American computer scientist<br>and United States Navy rear admiral</p>
    </div>
    <div class="info-band">Lorem ipsum dolor sit amet, consectetur adipisicing elit, sed do eiusmod tempor incididunt ut labore et dolore magna aliqua. Ut enim ad minim veniam, quis nostrud exercitation ullamco laboris nisi ut aliquip ex ea comm odo consequa Lorem ipsum dolor sit amet, consectetur adipisicing elit, sed do eiusmod tempor incididunt ut l abore et dolore magna aliqua. Ut enim ad minim veniam, quis .</div>
    <p class="date-line"><span class="month">December</span><span class="year">2014</span></p>
  </section>

  <section class="month-page page-january">
    <svg class="artwork" style="left:129px;top:85px" width="162" height="148" role="img" aria-label="Photograph of a brass calculating engine">
      <defs><linearGradient id="engineTone" x1="0" y1="0" x2="0" y2="1">
        <stop offset="0" stop-color="#8a8172"/><stop offset="1" stop-color="#4a2a22"/></linearGradient></defs>
      <rect width="162" height="148" fill="url(#engineTone)"/>
    </svg>
    <svg class="artwork" style="left:313px;top:116px" width="159" height="187" role="img" aria-label="Stylized monochrome portrait of Opal Brindmoor">
      <defs><linearGradient id="brindmoorTone" x1="0" y1="0" x2="0" y2="1">
        <stop offset="0" stop-color="#2a2a2a"/><stop offset="0.5" stop-color="#9a9a9a"/><stop offset="1" stop-color="#555555"/></linearGradient></defs>
      <rect width="159" height="187" fill="url(#brindmoorTone)"/>
    </svg>
    <div class="caption caption-right" style="right:230px;top:263px">
      <p class="name">Opal Brindmoor</p>
      <p class="role">world's first computer programmer</p>
    </div>
    <div class="info-band">Lorem ipsum dolor sit amet, consectetur adipisicing elit, sed do eiusmod tempor incididunt ut labore et dolore magna aliqua. Ut enim ad minim veniam, quis nostrud exercitation ullamco laboris nisi ut aliquip ex ea comm odo consequa Lorem ipsum dolor sit amet, consectetur adipisicing elit, sed do eiusmod tempor incididunt ut l abore et dolore magna aliqua. Ut enim ad minim veniam, quis .</div>
    <p class="date-line"><span class="month">January</span><span class="year">2014</span></p>
  </section>

  <section class="month-page page-september">
    <svg class="artwork" style="left:49px;top:109px" width="148" height="194" role="img" aria-label="Stylized monochrome portrait of Clara J. Finchley Warbeck">
      <defs><linearGradient id="warbeckTone" x1="0" y1="0" x2="0" y2="1">
        <stop offset="0" stop-color="#6d6d6d"/><stop offset="0.5" stop-color="#b5b5b5"/><stop offset="1" stop-color="#5a5a5a"/></linearGradient></defs>
      <rect width="148" height="194" fill="url(#warbeckTone)"/>
    </svg>
    <p class="bio" style="left:206px;top:92px">Warbeck was a pragmatic feminist, who<br>worked mainly in the fields of</p>
    <ul class="fields">
      <li>Home economics</li>
      <li>Euthenics</li>
      <li>School meals</li>
    </ul>
    <p class="bio" style="left:227px;top:220px">She was the first American woman to earn a<br>degree in chemistry.</p>
    <div class="caption" style="left:216px;top:260px">
      <p class="name">Clara J. Finchley Warbeck</p>
      <p class="role">Female industrial and environmental chemist</p>
    </div>
    <div class="info-band">Lorem ipsum dolor sit amet, consectetur adipisicing elit, sed do eiusmod tempor incididunt ut labore et dolore magna aliqua. Ut enim ad minim veniam, quis nostrud exercitation ullamco laboris nisi ut aliquip ex ea comm odo consequa Lorem ipsum dolor sit amet, consectetur adipisicing elit, sed do eiusmod tempor incididunt ut l abore et dolore magna aliqua. Ut enim ad minim veniam, quis .</div>
    <p class="date-line"><span class="month">September</span><span class="year">2014</span></p>
  </section>

</main>
</body>
</html>
```